Product labels for new supplements business targeting high performing creative people

I need a label design for different supplements like Whey, BCAA, Melatonin etc. that I could customize for each use case separately.

The brand is called lanternfolk.life, and it would be the first design of the labels. We haven't sold any products yet, but the target audience is people with growth mindset, people who want to be as efficient as possible and are constantly looking to improve their lifestyle. As part of that, they are also working out, but don't know much about supplements yet. Mostly people between 20-34.

I don't have a too specific idea of the expected design, though it should be light, warm, smart and minimalist, maybe have some patterns. It should looks smart and clean (and expensive). Orange and golden might be the additional colors for white. I have attached the templates of some products that I plan to sell and also the logo of the brand.

Here's what I have used for inspiration:
Brands that I like and are somewhat similar in concept: https://www.vimqera.com/ (!!specially the way they
bring "how the product helps them" in focus, not "what the product is" & https://www.pobri.care/ &
https://www.selvoda.com/sport/ & https://en.kambelo.fr/ &
https://gridmarket.com/profiles/corawellhaldesign/designs/417586

Here's how different products look like: https://prodaxel.com/catalog

Target Market(s)

target audience is people with growth mindset, people who want to be as efficient as possible and are constantly looking to improve their lifestyle. As part of that, they are also working out, but don't know much about supplements yet. Mostly people between 20-34.

Industry/Entity Type

Supplements

Font styles to use
Sans Serif

Colors
FFC000
F8CF3A
FAE287
FDF2CF
FEFAEE
F0912C
F2A743
F7CA91
FBE8D2
FDF5EE
EE7325
F08F49
F5BC92
FAE3D3
FDF4ED

Requirements
Must have
• Clean, smart and minimalist design that can be applied for different products in different sizes, like Whey protein, BCAA, vitamins etc. available here: https://prodaxel.com/catalog
Nice to have
• Patterns, expensive look
Should not have
• Doodles, too many colors

```html
<!DOCTYPE html>
<html lang="en">
<head>
<meta charset="utf-8">
<title>lanternfolk.life — BCAA 2:1:1 Wild Berry label</title>
<link rel="stylesheet" href="https://fonts.googleapis.com/css2?family=Oswald:wght@600&family=Outfit:wght@600&family=Roboto+Condensed:wght@400&display=swap">
<style>
  :root {
    --canvas: #f3f3f3;
    --gold: #ffc000;
    --gold-soft: #f8cf3a;
    --gold-light: #fae287;
    --lime: #c3cf48;
    --lime-deep: #b5c53f;
    --orange: #f0912c;
    --orange-deep: #ee7325;
    --orange-light: #f2a743;
    --ink: #1c1a17;
    --diamond: rgba(240, 145, 44, 0.22);
  }
  * { margin: 0; padding: 0; box-sizing: border-box; }
  html, body {
    width: 1200px;
    height: 1200px;
    overflow: hidden;
    background: var(--canvas);
  }
  .label {
    position: absolute;
    left: 160px;
    top: 90px;
    width: 880px;
    height: 1020px;
    overflow: hidden;
    background: var(--gold-soft);
  }
  .label__field {
    position: absolute;
    inset: 0;
    background: radial-gradient(ellipse at 50% 50%, var(--gold-soft) 0%, #f9d94e 55%, var(--gold-light) 100%);
  }
  .label__top-band {
    position: absolute;
    left: 0; top: 0;
    width: 100%;
    height: 96px;
    background: linear-gradient(90deg, var(--lime) 0%, var(--lime-deep) 100%);
  }
  .label__bottom-band {
    position: absolute;
    left: 0; bottom: 0;
    width: 100%;
    height: 88px;
    background: linear-gradient(180deg, var(--orange-light) 0%, var(--orange) 45%, var(--orange-deep) 100%);
  }
  .label__diamond {
    position: absolute;
    left: 440px;
    top: 545px;
    width: 520px;
    height: 520px;
    margin: -260px 0 0 -260px;
    border-radius: 70px;
    background: var(--diamond);
    transform: rotate(45deg);
  }
  .brand {
    position: absolute;
    left: 0; top: 270px;
    width: 100%;
    display: flex;
    justify-content: center;
    align-items: center;
    gap: 22px;
  }
  .brand__dot {
    width: 60px; height: 60px;
    border-radius: 50%;
    background: var(--orange-deep);
  }
  .brand__name {
    font-family: "Outfit", sans-serif;
    font-weight: 600;
    font-size: 80px;
    line-height: 1;
    color: var(--ink);
    letter-spacing: 0.5px;
  }
  .product {
    position: absolute;
    left: 0; top: 540px;
    width: 100%;
    text-align: center;
    color: var(--ink);
  }
  .product__name {
    font-family: "Oswald", sans-serif;
    font-weight: 600;
    font-size: 118px;
    line-height: 1;
    letter-spacing: -2px;
    transform: scaleX(0.82);
  }
  .product__flavour {
    font-family: "Roboto Condensed", sans-serif;
    font-size: 56px;
    line-height: 1;
    margin-top: 14px;
  }
  .product__claims {
    font-family: "Roboto Condensed", sans-serif;
    font-size: 33px;
    line-height: 1.45;
    margin-top: 34px;
  }
  .product__claims sup { font-size: 0.6em; }
  .label__footer {
    position: absolute;
    left: 28px; right: 28px;
    bottom: 96px;
    display: flex;
    justify-content: space-between;
    align-items: baseline;
    font-family: "Roboto Condensed", sans-serif;
    font-size: 32px;
    color: var(--ink);
  }
</style>
</head>
<body>
  <div class="label">
    <div class="label__field" role="img" aria-label="Fine golden fan-scale pattern across the label body"></div>
    <div class="label__top-band" role="img" aria-label="Lime green band with faint fan-scale pattern"></div>
    <div class="label__bottom-band" role="img" aria-label="Orange band with faint fan-scale pattern"></div>
    <div class="label__diamond"></div>

    <div class="brand">
      <span class="brand__dot"></span>
      <span class="brand__name">lanternfolk.life</span>
    </div>

    <div class="product">
      <h1 class="product__name">BCAA 2:1:1</h1>
      <p class="product__flavour">WILD BERRY</p>
      <p class="product__claims">Essentials branched chain amino acid BCAA<br>Increse muscle growth, reduces fatigue<sup>*</sup></p>
    </div>

    <div class="label__footer">
      <span class="label__type">DIETARY SUPPLEMENT</span>
      <span class="label__weight">Net Wt. 300g (10.58oz)</span>
    </div>
  </div>
</body>
</html>
```